BRAVOLK PROMOTION GROUP Website

Looking for a website design that clearly and powerfully portrays our unique and effective indoor advertising billboards in our network.

Our TeenyPanels, LargoPanels and TitanFlags are strategically placed in high traffic areas of restaurants, pubs, nightclubs, fitness clubs, colleges and universities, and sports arenas.

Bravolk Promotion Group is our new name. Our current site is www.plorvex.ca with our focus now being entirely on our Out-of-Home media. New website address will be www.bravolkpromotion.ca

We need the following sections:

HOME
PRODUCTS (Drop down menu)
-TeenyPanels
-LargoPanels
-TitanFlags
NETWORKS (Drop down menu)
-Resto-Bar
-Sports
-Campus
EFFECTIVENESS
CAMPAIGNS *This page will show numerous ad campaigns and could be a slide show (see www.plorvex.ca/QJPV_campaigns.html )
BECOME A PARTNER
CONTACT

Please include social media functions on the homepage such as chirpnet/visagebook/workloop

We will be supplying content and photos as required.

Our plan is to have you submit the homepage design to start with, and then we can start judging which styles we like the best and can start narrowing our list. As a second round, we would like to ask the "finalists" to submit a second page (another section of the website) and to see how consistent you are in terms of the look and feel you proposed for the homepage.

Attached is our new logo.

We may require you to upload the final website for us.

Websites that are in similar industry are:
www.trelmuk.com
www.quasplen.com

Industry/Entity Type

Advertising

Requirements
Must have
• Our network offers advertising solutions that feature: Guaranteed Readership,100% Gender Specific, Frequency, and Captive Audience. Purchasing advertising space in our network are small to medium business owners and advertising agencies booking on behalf of their clients.

Site must be professional and modern looking.
Nice to have
• Moving banner or slide show of some type.

```html
<!DOCTYPE html>
<html lang="en">
<head>
<meta charset="utf-8">
<title>Bravolk Promotion Group</title>
<link href="https://fonts.googleapis.com/css2?family=PT+Sans+Narrow&family=Source+Sans+3:ital,wght@0,400;0,600;1,400;1,600&display=swap" rel="stylesheet">
<style>
:root{
  --blue:#2c6bb5;
  --link:#1f5fae;
  --text:#333;
  --grey-panel:#e9e8e8;
  --line:#d6d6d6;
  --bg:#fff;
}
*{margin:0;padding:0;box-sizing:border-box}
html,body{width:1200px;height:1042px;overflow:hidden;background:var(--bg)}
body{position:relative;font-family:"Source Sans 3",sans-serif;color:var(--text);font-size:12px;
  background:linear-gradient(#f1f1f1,#fff 90px)}
.abs{position:absolute}

.brand{left:166px;top:20px;display:flex;align-items:center;gap:8px}
.brand-mark{width:22px;height:22px;background:var(--blue)}
.brand-name{font-family:"PT Sans Narrow",sans-serif;font-size:20px;color:#6b6b6b;line-height:1.05;width:140px}

.search{left:869px;top:10px;width:168px;height:20px;background:#e4e4e4;color:#4a6c9a;font-size:10px;padding:3px 8px}

.nav{left:345px;top:42px;width:692px;height:35px;border-top:1px solid var(--line);border-bottom:1px solid var(--line);display:flex;list-style:none}
.nav li{flex:auto;text-align:center;font-size:10.5px;border-left:1px solid #bbb;margin:4px 0;line-height:26px;white-space:nowrap}
.nav li:first-child{border-left:0;color:var(--blue)}
.nav .has-menu::after{content:"";display:inline-block;margin-left:5px;vertical-align:middle;border:3px solid transparent;border-top:4px solid #666;border-bottom:0}

.hero{left:168px;top:89px;width:647px;height:320px;background:linear-gradient(160deg,#9aa49a 0%,#7d8a6f 35%,#b64a3c 55%,#8a9a70 70%,#b6ae9c 100%)}
.hero-arrow{top:145px;width:36px;height:36px;border-radius:50%;background:rgba(255,255,255,.3)}
.hero-shadow{left:190px;top:409px;width:600px;height:16px;background:radial-gradient(ellipse at top,rgba(0,0,0,.18),transparent 70%)}
.intro{left:819px;top:89px;width:221px;height:320px;background:var(--grey-panel);padding:36px 20px 36px 16px}
.intro p{font-size:11.5px;line-height:20px;color:#222;margin-bottom:18px;width:180px}
.intro ul{list-style:none}
.intro li{font-family:"PT Sans Narrow",sans-serif;font-size:14px;color:var(--link);line-height:26px;padding-left:19px;position:relative}
.intro li::before{content:"";position:absolute;left:2px;top:11px;border:2px solid transparent;border-left:3px solid var(--link)}

.col-head{top:434px;height:39px;background:var(--blue);color:#fff;font-family:"PT Sans Narrow",sans-serif;font-size:18px;padding:8px 14px}
.thumb{border:1px solid #ccc}
.col-text{font-size:12px;line-height:16.6px;color:#333}
.more{font-style:italic;font-weight:600;font-size:13px;color:var(--link)}
.rule{height:30px;border-top:1px solid #e2e2e2;border-bottom:1px solid #e2e2e2;text-align:right;line-height:27px}
.uni{font-style:italic;font-weight:600;color:var(--link);font-size:11.5px;line-height:16.6px}
.cap{font-family:"PT Sans Narrow",sans-serif;font-size:14px;color:var(--link);text-align:center;width:82px}

.panel{left:167px;top:678px;width:873px;height:236px;background:#fff;box-shadow:0 0 14px rgba(0,0,0,.18)}
.panel-divider{left:702px;top:678px;width:1px;height:236px;background:#e0e0e0}
.panel-title{font-family:"PT Sans Narrow",sans-serif;font-size:18px;color:var(--link);border-bottom:1px solid #bbb;padding-bottom:6px}
.contact-row{font-size:11.5px;color:var(--link);line-height:26px}
.contact-row span{display:inline-block}

.footer{left:167px;top:939px;width:874px;height:97px;border:1px solid #ddd;text-align:center;font-style:italic;font-size:11px;color:#222;padding-top:14px;line-height:22px}
.social{display:flex;justify-content:center;gap:18px;font-style:normal;color:var(--link)}
.social span{display:flex;align-items:center;gap:5px}
.social span::before{content:"";width:9px;height:9px;background:var(--blue)}
</style>
</head>
<body>

<div class="abs brand"><span class="brand-mark"></span><span class="brand-name">Bravolk Promotion Group</span></div>
<div class="abs search">search</div>
<ul class="abs nav">
  <li>Home</li><li class="has-menu">Products</li><li class="has-menu">Networks</li><li>Effectiveness</li><li>Campaigns</li><li>Become a Partner</li><li>Contact</li>
</ul>

<div class="abs hero" role="img" aria-label="Aerial photo of a university sports stadium with a red running track and green field">
  <span class="abs hero-arrow" style="left:8px"></span>
  <span class="abs hero-arrow" style="right:8px"></span>
  <svg class="abs" style="left:20px;top:155px" width="12" height="16"><path d="M9 2 3 8l6 6" fill="none" stroke="#fff" stroke-width="2"/></svg>
  <svg class="abs" style="right:20px;top:155px" width="12" height="16"><path d="M3 2l6 6-6 6" fill="none" stroke="#fff" stroke-width="2"/></svg>
</div>
<div class="abs hero-shadow"></div>
<div class="abs intro">
  <p>We are a company specializing in the development of contractually obligated income for public and private groups.</p>
  <ul>
    <li>Sponsorship Programs</li><li>Venue Advertising</li><li>Facility Naming Rights</li>
    <li>Sponsorship Inventory Analysis</li><li>Vendor Rights</li><li>Out-of-Home Media</li>
  </ul>
</div>

<div class="abs col-head" style="left:167px;width:275px">Out Of Home</div>
<div class="abs thumb" role="img" aria-label="Photo of a backlit ad sign mounted in a washroom" style="left:168px;top:487px;width:115px;height:108px;background:linear-gradient(135deg,#d9d6cf,#aeb2b4 60%,#e8e8e6)"></div>
<p class="abs col-text" style="left:298px;top:486px;width:142px">48" x 72" backlit signs that are placed in high traffic common areas in cafeterias, student pubs and student centres, on College and University campuses.</p>
<div class="abs rule" style="left:167px;top:624px;width:275px"><span class="more">Learn More</span></div>

<div class="abs col-head" style="left:465px;width:275px">Networks</div>
<div class="abs thumb" role="img" aria-label="Photo of a modern glass university building" style="left:466px;top:487px;width:115px;height:108px;background:linear-gradient(160deg,#cfe0f0,#7e98b4 55%,#c7c9c4)"></div>
<div class="abs" style="left:600px;top:490px;width:142px">
  <div class="uni">NORVALE RIDGE<br>UNIVERSITY</div>
  <p class="col-text" style="margin-top:4px">Dunmere, BC</p>
  <p class="col-text" style="margin-top:5px">British Columbia's fourth largest university.</p>
  <p class="col-text" style="margin-top:5px">On-campus population of over 9,000 students.</p>
</div>
<div class="abs rule" style="left:469px;top:624px;width:275px"><span class="more">Learn More</span></div>

<div class="abs col-head" style="left:764px;width:275px">Campaigns</div>
<div class="abs thumb" role="img" aria-label="Framed ad poster for a denim brand" style="left:767px;top:490px;width:81px;height:100px;background:linear-gradient(#8a8178,#5a5654);border:2px solid #555"></div>
<div class="abs thumb" role="img" aria-label="Framed green ad poster for a junk removal service" style="left:862px;top:489px;width:81px;height:100px;background:linear-gradient(#7dbb55,#5e9c3a);border:2px solid #555"></div>
<div class="abs thumb" role="img" aria-label="Framed ad poster showing beer bottles" style="left:959px;top:490px;width:79px;height:98px;background:linear-gradient(#8b9aa8,#c3cbd2);border:2px solid #555"></div>
<div class="abs cap" style="left:761px;top:596px">Dennow</div>
<div class="abs cap" style="left:857px;top:596px">Haulrite</div>
<div class="abs cap" style="left:954px;top:596px">Frostbrew</div>
<div class="abs rule" style="left:768px;top:624px;width:275px"><span class="more">Learn More</span></div>

<div class="abs panel"></div>
<div class="abs panel-divider"></div>
<div class="abs panel-title" style="left:198px;top:699px;width:460px">Results</div>
<div class="abs" role="img" aria-label="Photo of an arena exterior under a blue sky" style="left:198px;top:752px;width:126px;height:118px;background:linear-gradient(#3f6fb6 0%,#8fb0d8 45%,#cfc9b6 60%,#5a5d57 100%)"></div>
<div class="abs col-text" style="left:340px;top:750px;width:320px">
  <p>The Q &amp; J Media Team negotiated the naming rights agreement for Sprintmark Place. The City of Dunmere received $525,000 over 5 years.</p>
  <p style="margin-top:10px">The Q &amp; J Media Team was the negotiator in the awarding to The Fizzora Bottling Group of a 10-year pouring rights agreement at all city facilities. The City of Dunmere receives over 1,000,000 over 10 years.</p>
</div>
<div class="abs more" style="left:341px;top:885px">Learn More</div>

<div class="abs panel-title" style="left:747px;top:699px;width:260px">Contact Us</div>
<div class="abs" style="left:748px;top:757px;font-size:13px;color:#111">4821-19B Avenue, Tallmoor, B.C. V0X 2K4</div>
<div class="abs" style="left:749px;top:782px">
  <div class="contact-row"><span style="width:62px">Telephone:</span>(604) 555-0147</div>
  <div class="contact-row"><span style="width:58px">Toll Free:</span>(888) 555-0193</div>
  <div class="contact-row"><span style="width:53px">Fax:</span>(604) 555-0162</div>
  <div class="contact-row"><span style="width:57px">E-mail:</span>info@plorvex.ca</div>
</div>

<div class="abs footer">
  <div>Home &nbsp;| &nbsp;Products &nbsp;| &nbsp;Networks &nbsp;| &nbsp;Effectiveness &nbsp;| &nbsp;Campaigns &nbsp;| &nbsp;Become a Partner &nbsp;| &nbsp;Contact</div>
  <div class="social"><span>chirpnet</span><span>visagebook</span><span>workloop</span></div>
  <div>Copyrights @ 2012 All Rights Reserved</div>
</div>

</body>
</html>
```